Construction business card

I need a new business card, they can connect with my logo, brand.
What we do is residential house , design and build
I like: Navy blue / black
I attached our logo, brand,
and, some idea for business card.

```html
<!DOCTYPE html>
<html lang="en">
<head>
<meta charset="utf-8">
<title>Harbour Building Group – Business Card</title>
<link rel="stylesheet" href="https://fonts.googleapis.com/css2?family=Jost:wght@400;500;600&display=swap">
<style>
  :root {
    --stage: #2b2b2c;
    --card: #222326;
    --card-deep: #0f1312;
    --ink-light: #ffffff;
    --ink-soft: #e6e6e6;
    --accent-blue: #3a86c8;
    --line-white: #ffffff;
  }
  html, body {
    margin: 0;
    padding: 0;
    width: 1200px;
    height: 900px;
    overflow: hidden;
    background: var(--stage);
  }
  .canvas {
    position: relative;
    width: 1200px;
    height: 900px;
    font-family: "Jost", "Futura", sans-serif;
  }
  .card {
    position: absolute;
    top: 301px;
    width: 515px;
    height: 296px;
    background: var(--card);
    overflow: hidden;
  }
  .card--front { left: 72px; }
  .card--back { left: 614px; }

  /* Front */
  .brand {
    position: absolute;
    inset: 0;
    display: flex;
    align-items: center;
    justify-content: center;
    gap: 12px;
  }
  .brand__mark {
    width: 18px;
    height: 18px;
    background: var(--accent-blue);
  }
  .brand__name {
    color: var(--ink-light);
    font-weight: 600;
    font-size: 27px;
    letter-spacing: 0.04em;
    text-transform: uppercase;
  }

  /* Back */
  .contact-person {
    position: absolute;
    left: 39px;
    top: 34px;
    color: var(--ink-light);
  }
  .contact-person__name {
    font-size: 19px;
    font-weight: 400;
    line-height: 1.1;
  }
  .contact-person__role {
    font-size: 13px;
    line-height: 1.3;
  }
  .contact-lines {
    position: absolute;
    right: 36px;
    top: 35px;
    text-align: right;
    color: var(--ink-light);
    font-size: 14px;
    line-height: 1.45;
  }
  .feature-art {
    position: absolute;
    left: 0;
    top: 88px;
    width: 515px;
    height: 178px;
    background: linear-gradient(120deg, #111213 0%, #2a2b2e 45%, #4a4b4e 70%, #2a2b2e 100%);
    opacity: 0.85;
  }
  .address-band {
    position: absolute;
    left: 0;
    bottom: 0;
    width: 515px;
    height: 40px;
  }
  .address {
    position: absolute;
    right: 34px;
    bottom: 6px;
    color: var(--ink-light);
    font-size: 17px;
  }
</style>
</head>
<body>
<main class="canvas">
  <section class="card card--front" aria-label="Card front">
    <div class="brand">
      <span class="brand__mark"></span>
      <span class="brand__name">Harbour Building Group</span>
    </div>
  </section>

  <section class="card card--back" aria-label="Card back">
    <div class="feature-art" role="img" aria-label="Dark abstract roofline graphic"></div>

    <div class="contact-person">
      <div class="contact-person__name">Daniel Harwood</div>
      <div class="contact-person__role">managing director</div>
    </div>
    <div class="contact-lines">
      <div>0400 555 018</div>
      <div>harbourbuildgroup.com.au</div>
    </div>

    <svg class="address-band" viewBox="0 0 515 40" aria-hidden="true">
      <polygon points="140,5 515,5 515,40 100,40" fill="var(--card-deep)"/>
      <polyline points="98,40 138,3 515,3" fill="none" stroke="var(--line-white)" stroke-width="5"/>
    </svg>
    <div class="address">27 Sample Rd., Oakvale, Vic 3100</div>
  </section>
</main>
</body>
</html>
```